Timeline flyer

Hi, we are an agency, our business is to orienteates student to study abroad in Germany. For that, we enroll them in language schools in Germany and help them to find an accomodation.
Students are always lost we thinked about a timeline to help them figure out what they have to do once in Germany so they don't miss delays.
You can find in the attachement an example that i made in powerpoint but it's really basic and it's only for u so you can understant what the timeline should look like.
We need two time lines.
For the first one (file first timeline)
Title : Procédure pour intégrer le semestre d’hiver dans les universités Allemandes
The first paragraph (up on the left in my proposition) : L’étudiant devra pendant ces mois débuter ses cours d’allemand en Tunisie et les poursuivre en Allemagne après l’obtention du Visa d’étude. L’atteinte du niveau C1 est primordiale pour la bonne réussite du test Kel ou le VRM.
The second paragraph (below on the left in my proposition) : L’étudiant devra à cette date avoir déjà passer le test KEL ou le VRM pour pouvoir être à temps pour les inscriptions universitaires. Il faut compter 6 semaines pour le test Kel et 2 à 3 semaines pour obtenir les résultats des tests.
The third one (up on the right in my proposition) : Le dernier délais d’inscription pour pouvoir intégrer une université Allemande pendant la rentrée hivernale (15 Octobre).
The last one (below on the right in my proposition) : Rentrée universitaire
For the second one (file second timeline) :
Title : Procédure pour intégrer le semestre d’été dans les universités Allemandes *
The third one (up on the right in my proposition) : Le dernier délais d’inscription pour pouvoir intégrer une université Allemande pendant la rentrée estivale (15 Avril).
There is also an additional sentence below in the right for this one : * Les spécialités assurées pendant les semestres d’été sont limitées.
You can also find in the attachement our flyers (so you can inspire youself with the color and the design), we want our student to recognize that the flyer is related to our agency so please try to use colors that are matched with the other flyer.
Also, you can find our Logo in the attachement.
Thank you :)
Waiting for your propositions ! :)

```html
<!DOCTYPE html>
<html lang="fr">
<head>
<meta charset="utf-8">
<title>Calendrier semestres – Lernweg Centre</title>
<link href="https://fonts.googleapis.com/css2?family=Roboto:wght@400;500;700&family=Roboto+Condensed:wght@700&display=swap" rel="stylesheet">
<style>
:root{
  --page:#d4d4d6;
  --cream-a:#f7eed0;--cream-b:#faf5de;
  --brown:#6f5653;--brown-title:#8d6b5c;
  --tan:#dec8a0;--pale:#efe7bd;--tan-border:#e2cfa8;
  --orange:#e29a3c;--lime:#c4d22e;--ink:#111;--text:#4a4036;
}
*{margin:0;padding:0;box-sizing:border-box}
html,body{width:891px;height:1200px;overflow:hidden;background:var(--page);font-family:"Roboto",sans-serif}
.flyer{position:absolute;left:86px;width:720px;height:507px;overflow:hidden}
.flyer--winter{top:86px;background:linear-gradient(135deg,var(--cream-a),var(--cream-b))}
.flyer--summer{top:607px;background:#fff}
.flyer > *{position:absolute}
.brand{left:34px;top:60px;font:700 30px/1 "Roboto Condensed",sans-serif;letter-spacing:-.5px}
.brand small{display:block;font-size:17px;margin:2px 0 0 44px}
.brand-dot{left:18px;top:66px;width:10px;height:10px;border-radius:50%}
.flyer--winter .brand{color:#5a4a44}.flyer--winter .brand small{color:#d9bf94}.flyer--winter .brand-dot{background:#e3cca3}
.flyer--summer .brand{color:#3a3a3a}.flyer--summer .brand small{color:#a8b520}.flyer--summer .brand-dot{background:var(--lime)}
.title{left:270px;top:56px;width:440px;font:700 21.5px/27px "Roboto",sans-serif}
.title sup{font-size:9px}
.flyer--winter .title{color:var(--brown-title)}.flyer--summer .title{color:var(--ink)}
.note{border:1px solid var(--tan-border);border-radius:8px;background:rgba(255,255,255,.25);padding:7px 8px;font-size:9.8px;line-height:12.6px;color:var(--text);text-align:justify}
.note--plan{left:42px;top:149px;width:279px;height:71px}
.note--deadline{left:485px;top:149px;width:159px;height:71px}
.note--exam{left:82px;top:382px;width:279px;height:71px}
.note--start{left:400px;top:382px;width:158px;height:71px;display:flex;align-items:center;justify-content:center;font:500 13px/1 "Roboto",sans-serif;color:var(--brown-title)}
.links{left:0;top:0;width:720px;height:507px}
.band{left:42px;top:249px;width:600px;height:104px;border-radius:5px;overflow:hidden;display:grid;grid-template-columns:repeat(15,40px)}
.cell{background:var(--tan);display:flex;align-items:center;justify-content:center}
.cell:nth-child(even){background:var(--pale)}
.month{writing-mode:vertical-rl;transform:rotate(180deg);font:700 10.5px/1 "Roboto",sans-serif;color:var(--brown);white-space:nowrap}
.flyer--summer .month{color:#5b4a3e}
.milestone{top:244px;width:44px;height:114px;border-radius:12px;color:#fff;font:700 12.3px/14.5px "Roboto",sans-serif;text-align:center;display:flex;align-items:center;justify-content:center}
.flyer--winter .milestone{background:var(--brown)}.flyer--summer .milestone{background:var(--orange)}
.m1{left:360px}.m2{left:440px}.m3{left:558px;width:52px}
.laptop{left:10px;top:462px;width:40px;height:30px;border-radius:3px}
.flyer--winter .laptop{background:linear-gradient(#e6d8b8,#cdbb96)}
.flyer--summer .laptop{background:linear-gradient(#eee,#ccc)}
.graduates{left:586px;top:372px;width:108px;height:98px;border-radius:10px;background:radial-gradient(circle,#efe2c2,rgba(247,238,208,0))}
.footer{left:42px;top:473px;width:660px;height:16px;border-radius:8px;color:#fff;font-size:8.4px;line-height:16px;padding:0 12px 0 15px}
.footer b{font-weight:700}
.footer .web{position:absolute;right:12px;top:0;display:flex;align-items:center;gap:4px}
.footer .web i{display:inline-block;width:7px;height:7px;background:#fff;border-radius:1px}
.flyer--winter .footer{background:var(--brown)}.flyer--summer .footer{background:#000}
.footnote{left:580px;top:437px;width:120px;font-size:6.6px;line-height:8.5px;color:#555;text-align:right}
</style>
</head>
<body>

<section class="flyer flyer--winter">
  <div class="brand-dot"></div>
  <div class="brand">lernweg<small>centre</small></div>
  <h1 class="title">Procédure pour intégrer le semestre d'hiver dans les universités Allemandes</h1>

  <svg class="links" viewBox="0 0 720 507">
    <g fill="none" stroke="#d9a65a" stroke-width="1" stroke-dasharray="3 2">
      <path d="M321 186H344V249"/><path d="M485 184H462V244"/>
      <path d="M382 358V417H361"/><path d="M582 358V417H558"/>
    </g>
    <path d="M62 249V233H344" fill="none" stroke="#e2cfa8" stroke-width="1.5"/>
    <path d="M30 297H42V305H30Z" fill="#6f5653"/>
    <path d="M642 297H681L668 284L675 278L698 301L675 324L668 318L681 305H642Z" fill="#6f5653"/>
  </svg>

  <div class="band">
    <div class="cell"><b class="month">SEP 2016</b></div><div class="cell"><b class="month">OCT 2016</b></div><div class="cell"><b class="month">NOV 2016</b></div><div class="cell"><b class="month">DÉC 2016</b></div><div class="cell"><b class="month">JAN 2017</b></div><div class="cell"><b class="month">FÉV 2017</b></div><div class="cell"><b class="month">MARS 2017</b></div><div class="cell"><b class="month">AVR 2017</b></div><div class="cell"></div><div class="cell"><b class="month">JUI 2017</b></div><div class="cell"></div><div class="cell"><b class="month">AOÛT 2017</b></div><div class="cell"><b class="month">SEP 2017</b></div><div class="cell"></div><div class="cell"><b class="month">NOV 2017</b></div>
  </div>
  <div class="milestone m1">Debut<br>Mai<br>2017</div>
  <div class="milestone m2">15<br>Juillet<br>2017</div>
  <div class="milestone m3">15<br>Octobre<br>2017</div>

  <p class="note note--plan">L’étudiant devra pendant ces mois débuter ses cours d’allemand en Tunisie et les poursuivre en Allemagne après l’obtention du Visa d’étude. L’atteinte du niveau C1 est primordiale pour la bonne réussite du test Kel ou le VRM.</p>
  <p class="note note--deadline">Le dernier délais d’inscription pour pouvoir intégrer une université Allemande pendant la rentrée hivernale (15 Octobre).</p>
  <p class="note note--exam">L’étudiant devra à cette date avoir déjà passer le test KEL ou le VRM pour pouvoir être à temps pour les inscriptions universitaires. Il faut compter 6 semaines pour le test Kel et 2 à 3 semaines pour obtenir les résultats des tests.</p>
  <p class="note note--start">Rentrée universitaire</p>

  <div class="graduates" role="img" aria-label="Étudiants diplômés lançant leurs toques"></div>
  <div class="laptop" role="img" aria-label="Ordinateur portable"></div>
  <div class="footer">Pour plus d’informations contactez nous: <b>LERNWEG CENTRE</b> Tél. <b>70 123 456</b> Sfax : <b>74 210 555</b> / Sousse : <b>58 310 742</b><span class="web"><i></i>LERNWEG.ORG <i></i>LERNWEG</span></div>
</section>

<section class="flyer flyer--summer">
  <div class="brand-dot"></div>
  <div class="brand">lernweg<small>centre</small></div>
  <h1 class="title">Procédure pour intégrer le semestre d'été dans les universités Allemandes<sup>*</sup></h1>

  <svg class="links" viewBox="0 0 720 507">
    <g fill="none" stroke="#e29a3c" stroke-width="1" stroke-dasharray="3 2">
      <path d="M321 186H344V249"/><path d="M485 184H462V244"/>
      <path d="M382 358V417H361"/><path d="M582 358V417H558"/>
    </g>
    <path d="M62 249V233H344" fill="none" stroke="#e2cfa8" stroke-width="1.5"/>
    <path d="M30 297H42V305H30Z" fill="#e29a3c"/>
    <path d="M642 297H681L668 284L675 278L698 301L675 324L668 318L681 305H642Z" fill="#e29a3c"/>
  </svg>

  <div class="band">
    <div class="cell"><b class="month">MARS 2017</b></div><div class="cell"><b class="month">AVR 2017</b></div><div class="cell"><b class="month">MAI 2017</b></div><div class="cell"><b class="month">JUIN 2017</b></div><div class="cell"><b class="month">JUI 2017</b></div><div class="cell"><b class="month">AOÛT 2017</b></div><div class="cell"><b class="month">SEP 2017</b></div><div class="cell"><b class="month">OCT 2017</b></div><div class="cell"></div><div class="cell"><b class="month">DÉC 2016</b></div><div class="cell"></div><div class="cell"><b class="month">FÉV 2018</b></div><div class="cell"><b class="month">MARS 2018</b></div><div class="cell"></div><div class="cell"><b class="month">MAI 2018</b></div>
  </div>
  <div class="milestone m1">Debut<br>Nov<br>2017</div>
  <div class="milestone m2">15<br>Jan<br>2018</div>
  <div class="milestone m3">15<br>Avril<br>2018</div>

  <p class="note note--plan">L’étudiant devra pendant ces mois débuter ses cours d’allemand en Tunisie et les poursuivre en Allemagne après l’obtention du Visa d’étude. L’atteinte du niveau C1 est primordiale pour la bonne réussite du test Kel ou le VRM.</p>
  <p class="note note--deadline">Le dernier délais d’inscription pour pouvoir intégrer une université Allemande pendant la rentrée estivale (15 Avril).</p>
  <p class="note note--exam">L’étudiant devra à cette date avoir déjà passer le test KEL ou le VRM pour pouvoir être à temps pour les inscriptions universitaires. Il faut compter 6 semaines pour le test Kel et 2 à 3 semaines pour obtenir les résultats des tests.</p>
  <p class="note note--start">Rentrée universitaire</p>

  <p class="footnote">*Les spécialités assurées pendant les semestres d’été sont limitées.</p>
  <div class="laptop" role="img" aria-label="Ordinateur portable"></div>
  <div class="footer">Pour plus d’informations contactez nous: <b>LERNWEG CENTRE</b> Tél. <b>70 123 456</b> Sfax : <b>74 210 555</b> / Sousse : <b>58 310 742</b><span class="web"><i></i>LERNWEG.ORG <i></i>LERNWEG</span></div>
</section>

</body>
</html>
```